Business Card Project for Firm Deck Hoisting

Business name is "Firm Deck Hoisting" we are a scaffolding & rigging business specialising in local and remote work for:
- scaffolding (residential, commercial, industrial)
- rigging
-man material hoists
- swing stages
- labour hire

On the back of the card I would like FDH as the symbol / logo. I have attached the logos we have had created by sketch harbour. We would like to use bold colours – preferably as the same colour scheme as the logo.

Target Market(s)

Construction business

Industry/Entity Type

Construction

Contact Information for Business Card

name: Owen Pellew
Title: Director
Phone: 0491 572 864
Address: PO BOX 3251, Paralowie SA 5108
Email: owen@firmdeckhoisting.com.au
Website: www.firmdeckhoisting.com.au

Font styles to use
Sans Serif

Requirements
Must have
• Must use existing logo & prefering using bold colours
Nice to have
• Would be nice to have a line of dot points in what we specialise in but not essential
• Would be nice to see some designs with a slogan but not essential
Should not have
• NA

```html
<!DOCTYPE html>
<html lang="en">
<head>
<meta charset="UTF-8">
<title>Firm Deck Hoisting – Business Card</title>
<link href="https://fonts.googleapis.com/css2?family=Lato:wght@400;700&display=swap" rel="stylesheet">
<style>
  :root {
    --brand-blue: #2c73bd;
    --ink: #111111;
    --paper: #ffffff;
    --backdrop: #e9eaec;
  }
  * { box-sizing: border-box; margin: 0; padding: 0; }
  html, body {
    width: 1200px; height: 900px; overflow: hidden;
    background: var(--backdrop);
    font-family: "Lato", Arial, sans-serif;
  }
  .stage {
    width: 1200px; height: 900px;
    display: flex; align-items: center; justify-content: center; gap: 40px;
  }
  .card {
    position: relative;
    width: 540px; height: 330px;
    overflow: hidden;
    box-shadow: 0 8px 24px rgba(0,0,0,.18);
  }

  /* Front */
  .card-front { background: var(--paper); color: var(--ink); }
  .brand {
    display: flex; align-items: center; gap: 10px;
    font-weight: 700; letter-spacing: .5px;
  }
  .brand-square { width: 14px; height: 14px; flex: none; }
  .card-front .brand {
    position: absolute; left: 32px; top: 34px;
    color: var(--ink); font-size: 26px;
  }
  .card-front .brand-square { background: var(--brand-blue); }
  .contact-list {
    position: absolute; left: 32px; top: 110px;
    list-style: none; font-size: 15px; line-height: 23px;
  }
  .contact-list li { display: flex; align-items: center; gap: 9px; }
  .contact-icon { width: 13px; height: 13px; fill: var(--brand-blue); flex: none; }
  .person {
    position: absolute; right: 36px; top: 130px; text-align: right;
  }
  .person-name { color: var(--brand-blue); font-size: 27px; font-weight: 400; }
  .person-title { font-size: 17px; margin-top: 2px; }
  .address { font-size: 17px; margin-top: 18px; line-height: 22px; }
  .footer-band {
    position: absolute; left: 0; right: 0; bottom: 0; height: 34px;
    background: var(--brand-blue);
    border-top: 6px solid var(--ink);
  }

  /* Back */
  .card-back {
    background: var(--brand-blue); color: var(--paper);
    display: flex; flex-direction: column; align-items: center; justify-content: center;
  }
  .card-back .brand { color: var(--paper); font-size: 34px; }
  .card-back .brand-square { background: var(--paper); width: 18px; height: 18px; }
  .services {
    margin-top: 30px; text-align: center;
    font-size: 15px; line-height: 22px; padding: 0 30px;
  }
</style>
</head>
<body>
<main class="stage">

  <section class="card card-front">
    <div class="brand"><span class="brand-square"></span>FDH Firm Deck Hoisting</div>

    <ul class="contact-list">
      <li>
        <svg class="contact-icon" viewBox="0 0 24 24"><path d="M6.6 10.8a15.2 15.2 0 0 0 6.6 6.6l2.2-2.2a1 1 0 0 1 1-.25 11.4 11.4 0 0 0 3.6.57 1 1 0 0 1 1 1V20a1 1 0 0 1-1 1A17 17 0 0 1 3 4a1 1 0 0 1 1-1h3.5a1 1 0 0 1 1 1c0 1.25.2 2.45.57 3.57a1 1 0 0 1-.25 1z"/></svg>
        0491 572 864
      </li>
      <li>
        <svg class="contact-icon" viewBox="0 0 24 24"><path d="M2 5h20v14H2z M2 5l10 8 10-8" stroke="#fff" stroke-width="1.5"/></svg>
        owen@firmdeckhoisting.com.au
      </li>
      <li>
        <svg class="contact-icon" viewBox="0 0 24 24"><circle cx="12" cy="12" r="10"/><path d="M2 12h20M12 2c3 3 3 17 0 20M12 2c-3 3-3 17 0 20" stroke="#fff" stroke-width="1.3" fill="none"/></svg>
        www.firmdeckhoisting.com.au
      </li>
    </ul>

    <div class="person">
      <div class="person-name">Owen Pellew</div>
      <div class="person-title">Director</div>
      <div class="address">PO BOX 3251<br>Brindlewood SA 5112</div>
    </div>

    <div class="footer-band" aria-hidden="true"></div>
  </section>

  <section class="card card-back">
    <div class="brand"><span class="brand-square"></span>FDH Firm Deck Hoisting</div>
    <p class="services">
      scaffolding (residential, commercial, industrial)<br>
      • rigging • man material hoists • swing stages • labour hire
    </p>
  </section>

</main>
</body>
</html>
```